CBD Oil manufacturer needs a label/logo.

We need a label/logo design for our CBD oil bottles. The brand name is Velsora - meaning immortality. CBD oil is made from the hemp plant, usually used medicinally. We are open to color schemes and designs. I am attaching a label that someone else made - but we do not like at all. The information listed on the side does need to be included.

Target Market(s)

CBD Oil Retailers - generally for medicinal purposes. Geared towards all ages, etc.

Industry/Entity Type

Manufacturer

Requirements
Must have
• Supplement Facts, Suggested use, Other Ingredients, Manufactured by, etc. AS SEEN ON ATTACHMENT.

```html
<!DOCTYPE html>
<html lang="en">
<head>
<meta charset="utf-8">
<title>Velsora Hemp Label Set</title>
<link rel="stylesheet" href="https://fonts.googleapis.com/css2?family=Comfortaa:wght@300;700&family=Open+Sans:wght@400&display=swap">
<style>
  :root {
    --backdrop: #a09f9f;
    --label-black: #141414;
    --label-charcoal: #2a2a2a;
    --brand-green: #2e7d4f;
    --label-white: #f7f7f7;
    --text-light: #e9e9e9;
    --text-muted: #bdbdbd;
    --rule-gold: #a89466;
  }
  * { box-sizing: border-box; margin: 0; padding: 0; }
  html, body { width: 1200px; height: 1200px; overflow: hidden; }
  body {
    background: var(--backdrop);
    display: flex;
    align-items: center;
    justify-content: center;
    gap: 80px;
  }
  .label {
    position: relative;
    width: 420px;
    height: 560px;
    background: linear-gradient(90deg, var(--label-black) 0%, var(--label-charcoal) 50%, var(--label-black) 100%);
    overflow: hidden;
    border-radius: 6px;
  }
  .label__band {
    position: absolute;
    top: 0; left: 0; right: 0;
    height: 170px;
  }
  .label__arch {
    position: absolute;
    top: 0;
    left: 50%;
    transform: translateX(-50%);
    width: 270px;
    height: 330px;
    border-radius: 0 0 135px 135px;
  }
  .label--green .label__band,
  .label--green .label__arch { background: var(--brand-green); }
  .label--white .label__band,
  .label--white .label__arch { background: var(--label-white); }

  .brand-name {
    position: absolute;
    top: 196px;
    left: 0; right: 0;
    text-align: center;
    font-family: "Comfortaa", sans-serif;
    font-weight: 700;
    font-size: 38px;
    line-height: 1;
    letter-spacing: 2px;
  }
  .label--green .brand-name { color: var(--label-white); }
  .label--white .brand-name { color: var(--brand-green); }

  .label__info {
    position: absolute;
    top: 352px;
    left: 0; right: 0;
    text-align: center;
    color: var(--text-light);
  }
  .info__type {
    font-family: "Open Sans", sans-serif;
    font-size: 18px;
    color: var(--text-muted);
    letter-spacing: 1px;
  }
  .info__dose {
    font-family: "Comfortaa", sans-serif;
    font-weight: 300;
    font-size: 28px;
    margin-top: 6px;
  }
  .info__rule {
    width: 260px;
    height: 2px;
    margin: 12px auto;
    background: var(--text-light);
  }
  .label--white .info__rule { background: var(--rule-gold); }
  .info__product {
    font-family: "Comfortaa", sans-serif;
    font-weight: 700;
    font-size: 32px;
    line-height: 1.3;
    letter-spacing: 1px;
  }
  .info__contents {
    font-family: "Open Sans", sans-serif;
    font-size: 17px;
    color: var(--text-muted);
  }
</style>
</head>
<body>
  <section class="label label--green">
    <div class="label__band"></div>
    <div class="label__arch"></div>
    <p class="brand-name">VELSORA</p>
    <div class="label__info">
      <p class="info__type">HEMP</p>
      <p class="info__dose">1,000 mg</p>
      <div class="info__rule"></div>
      <p class="info__product">Cannabidiol</p>
      <div class="info__rule"></div>
      <p class="info__contents">whole hemp and coconut oils</p>
    </div>
  </section>

  <section class="label label--white">
    <div class="label__band"></div>
    <div class="label__arch"></div>
    <p class="brand-name">VELSORA</p>
    <div class="label__info">
      <p class="info__type">HEMP</p>
      <p class="info__dose">1,000 mg</p>
      <div class="info__rule"></div>
      <p class="info__product">Cannabidiol</p>
      <div class="info__rule"></div>
      <p class="info__contents">whole hemp and coconut oils</p>
    </div>
  </section>
</body>
</html>
```